The Steady HEART-Ledger Book Cover

Design a book cover that will eventually be part of an entire brand.
The book title: The Steady HEART-ledger
Subtitle: Fatherhood Across The Seasons Of The Restless Daughters.
I want it to look masculine, bold and inviting both online and on the shelf.
As much as it is a book for men. Women will be attracted to it as well. They make up over 60% of my fan base. They may buy it for the men in their life.
I do not have any files to upload as this is a first shot at getting the cover and brand started.
I am known as #YourGuideToGrit and a men and relationship expert. My mission is to inspire men to live remarkable lives.
Host of The Ironwood Fellow Hour and Founder of The Ironwood Fellow Circle.
This is my second book and feel that the time could not be better for this material.
I think a classy, even vintage/modern look would be great, but again I am open to ideas.
Corbin Heywood
Target Market(s)
Men 25-60 in transition. Couples going through breakup, separation or divorce. Men that want to find insights, inner peace and understanding themselves and women at a core level.
Font styles to use
Colors
Designer to choose colors to be used in the design.
Requirements
Must have
- Bold, creative, inviting
Nice to have
- Background Image that reflects the overall message
Should not have
- Too much artistic licence making it too busy.

```html
<!DOCTYPE html>
<html lang="en">
<head>
<meta charset="utf-8">
<title>The Steady HEART-Ledger — Book Cover</title>
<link rel="stylesheet" href="https://fonts.googleapis.com/css2?family=Oswald:wght@500;600&family=Roboto+Condensed:wght@400&display=swap">
<style>
  :root {
    --canvas-bg: #ffffff;
    --cover-bg: #f4f3f1;
    --title-ink: #33344a;
    --subtitle-ink: #2a2a2e;
    --author-ink: #ffffff;
    --glow: #fbeedb;
    --sun: #f2cf95;
    --dusk: #b9958c;
    --city: #6b6675;
    --city-deep: #3c3f52;
  }
  * { margin: 0; padding: 0; box-sizing: border-box; }
  html, body {
    width: 1200px;
    height: 1200px;
    overflow: hidden;
    background: var(--canvas-bg);
  }
  .book-cover {
    position: absolute;
    left: 240px;
    top: 60px;
    width: 720px;
    height: 1080px;
    background: var(--cover-bg);
    overflow: hidden;
  }
  .cover-art {
    position: absolute;
    left: 0;
    right: 0;
    top: 330px;
    bottom: 0;
    background:
      radial-gradient(ellipse 55% 40% at 45% 72%, rgba(255,236,200,0.9), rgba(255,236,200,0) 70%),
      linear-gradient(to bottom,
        rgba(244,243,241,1) 0%,
        var(--glow) 22%,
        var(--sun) 55%,
        var(--dusk) 72%,
        var(--city) 86%,
        var(--city-deep) 100%);
  }
  .cover-title {
    position: absolute;
    top: 70px;
    left: 0;
    right: 0;
    text-align: center;
    font-family: "Oswald", sans-serif;
    font-weight: 600;
    font-size: 96px;
    line-height: 1.08;
    letter-spacing: 1px;
    color: var(--title-ink);
    text-transform: uppercase;
  }
  .cover-subtitle {
    position: absolute;
    top: 305px;
    left: 0;
    right: 0;
    text-align: center;
    font-family: "Roboto Condensed", sans-serif;
    font-weight: 400;
    font-size: 25px;
    color: var(--subtitle-ink);
  }
  .cover-author {
    position: absolute;
    bottom: 42px;
    left: 0;
    right: 0;
    text-align: center;
    font-family: "Roboto Condensed", sans-serif;
    font-weight: 400;
    font-size: 32px;
    color: var(--author-ink);
  }
</style>
</head>
<body>
  <main class="book-cover">
    <div class="cover-art" role="img" aria-label="Photograph of a man in a suit seen from behind, with a sunlit city skyline blended into his silhouette"></div>
    <h1 class="cover-title">The Steady<br>HEART-Ledger</h1>
    <p class="cover-subtitle">Fatherhood Across The Seasons Of The Restless Daughters</p>
    <p class="cover-author">Corbin Heywood</p>
  </main>
</body>
</html>
```